Onboarding Infographic/brochure

We are a small criminal defense firm looking to create some sort of infographic or brochure that we can onboard new clients with. We are currently sending it out via email but want something a bit cooler and fun to send to clients. The information is:

A Few Quick Rules

We are here to help each step of the way. While questions are never discouraged, this letter will answer some of the most common ones we get asked.

Communications

As a client, you should always be in the loop. While we will try to respond to questions as quickly as possible, sometimes we are unable to respond right away. Do not worry - we promise to get back to you soon. Some questions might take some time to research, and a correct answer is better than a quick one.

Appointments

One of the benefits of having an attorney is the ability to discuss your case outside of court, minus the stress and headaches. If you need an appointment, please contact the office.

Appointments must be scheduled in advance. We do not want you to make a special trip to the office only to learn that we are in court or otherwise unavailable.

Jail Visits

If your family member is currently in jail, we take that very seriously. We will visit your loved one and introduce ourselves. While the case is ongoing, we ask that a family member be designated a “contact” person so that messages can be relayed quickly. Never discuss the facts of the case over the phone with someone who is in jail. Jail calls are recorded and we have seen too many cases go south based on remarks made over recorded lines.

Police Reports and Discovery

We will do our best to provide you with copies of everything we receive on your case. Most information will be emailed, so please keep your email address up to date.

Changes in Contact Information

If you move or change numbers during the case, please let us know. It is difficult to help if we are unable to reach you, and helping you is why we are here.

Court Appearances

Cases do not get resolved as quickly as they do on television. Expect there to be several hearings in your case and it may be necessary for you to attend one or more of them. If a hearing is set, you will receive notice of the date and time of each hearing.

Billing and Collections

We understand that this investment was a huge decision for you. As we focus on providing the best representation, we will need for you to stay on schedule with any payment arrangements agreed to at the time of your initial consultation.

Again, thank you for your trust in us. We look forward to getting a fantastic outcome on your case.

Target Market(s)

Criminal defense clients and their families

Industry/Entity Type

Legal

Font styles to use
Serif

Requirements
Must have
• Must incorporate all of the rules we email out. Would like diagrams, images or pictures
Nice to have
• We attached a Welcome brochure. Not sure I want it to look super similar, hence the request for infographic.

```html
<!DOCTYPE html>
<html lang="en">
<head>
<meta charset="utf-8">
<title>A Few Quick Rules – Harlow Legal Group</title>
<link rel="stylesheet" href="https://fonts.googleapis.com/css2?family=Archivo+Black&family=Rubik:ital,wght@0,400;0,600;1,600&display=swap">
<style>
:root{
  --page:#d4d5d7;
  --navy:#1c2d52;
  --navy-band:#2a3b5e;
  --gold:#c6a54a;
  --gold-text:#c9a646;
  --teal:#5e9c90;
  --paper:#f6f6f4;
  --ink:#1d2433;
  --white:#ffffff;
}
*{box-sizing:border-box;margin:0;padding:0}
html,body{width:1200px;height:2914px;overflow:hidden;background:var(--page)}
body{position:relative;font-family:"Rubik",sans-serif;color:var(--ink)}
.sheet{position:absolute;left:86px;top:77px;width:1027px;height:2759px;background:var(--paper);overflow:hidden}
.masthead{position:absolute;left:0;top:0;width:1027px;height:560px}
.masthead-curve{position:absolute;left:0;top:0}
.brand{position:absolute;top:50px;left:0;width:100%;text-align:center;font-family:"Archivo Black",sans-serif;font-size:38px;letter-spacing:2px;color:var(--white)}
.headline{position:absolute;top:142px;left:0;width:100%;text-align:center;font-family:"Archivo Black",sans-serif;font-size:54px;color:var(--gold-text);letter-spacing:-1px}
.intro{position:absolute;top:212px;left:148px;width:731px;text-align:center;font-size:28px;line-height:37px;color:var(--white)}
.seal{position:absolute;left:781px;top:321px;width:166px;height:166px;border-radius:50%;background:var(--navy);border:8px solid var(--gold);box-shadow:0 0 0 3px var(--white)}
.row{position:absolute;left:0;width:1027px}
.row.gold{background:var(--gold)}
.row.navy{background:var(--navy-band)}
.row.teal{background:var(--teal)}
.photo{position:absolute;width:415px;height:226px;border:3px solid var(--gold)}
.row.gold .photo{border-color:var(--white)}
.photo.left{left:76px}
.photo.right{left:537px}
.copy{position:absolute}
.copy.left{left:78px;width:415px}
.copy.right{left:538px;width:388px}
.copy h2{font-family:"Archivo Black",sans-serif;font-size:25px;line-height:32px;color:var(--gold-text);text-transform:uppercase;margin-bottom:12px;letter-spacing:.2px}
.copy p{font-size:17px;line-height:23.5px}
.copy p+p{margin-top:11px}
.copy .strong{font-weight:600}
.row.gold h2,.row.teal h2{color:var(--white)}
.row.gold p,.row.navy p,.row.teal p{color:var(--white)}
.thanks{position:absolute;left:78px;top:2583px;width:873px;height:46px;border:1.5px solid var(--gold);background:var(--white);text-align:center;font-style:italic;font-weight:600;font-size:17.5px;line-height:43px;color:var(--navy)}
.footer{position:absolute;left:0;top:2667px;width:1027px;height:92px;background:var(--navy);display:flex;align-items:center;justify-content:space-between;padding:0 76px 0 78px}
.contact{display:flex;align-items:center;gap:12px;color:var(--white);font-weight:600;font-size:20px}
.icon{width:46px;height:46px;border-radius:50%;background:var(--gold);display:flex;align-items:center;justify-content:center}
</style>
</head>
<body>
<main class="sheet">
  <header class="masthead">
    <svg class="masthead-curve" width="1027" height="560" viewBox="0 0 1027 560" aria-hidden="true">
      <defs>
        <linearGradient id="mastheadTone" x1="0" y1="0" x2="0" y2="1">
          <stop offset="0" stop-color="#1a2a4e"/>
          <stop offset="1" stop-color="#24365e"/>
        </linearGradient>
      </defs>
      <path d="M0,0 H1027 V345 Q513.5,585 0,345 Z" fill="var(--gold)"/>
      <path d="M0,0 H1027 V330 Q513.5,566 0,330 Z" fill="url(#mastheadTone)"/>
    </svg>
    <div class="brand">HARLOW LEGAL GROUP</div>
    <h1 class="headline">A FEW QUICK RULES</h1>
    <p class="intro">We are here to help each step of the way. While questions are never discouraged, this letter will answer some of the most common ones we get asked.</p>
    <div class="seal" role="img" aria-label="Badge"></div>
  </header>

  <section class="row" style="top:500px;height:261px">
    <div class="copy left" style="top:12px">
      <h2>Communications</h2>
      <p>As a client, you should always be in the loop.<br>While we will try to respond to questions as quickly as possible, sometimes we are unable to respond right away.</p>
      <p class="strong">Do not worry - we promise to get back to you soon. Some questions might take some time to research, and a correct answer is better than a quick one.</p>
    </div>
    <div class="photo right" style="top:9px;background:linear-gradient(135deg,#c9a07a,#3a3f4a 55%,#dcdfe2)" role="img" aria-label="Photo of an attorney reviewing a document with a client"></div>
  </section>

  <section class="row gold" style="top:761px;height:298px">
    <div class="photo left" style="top:33px;background:linear-gradient(135deg,#3e5a6e,#7b6a5c 50%,#c9b9a6)" role="img" aria-label="Photo of an attorney meeting clients around a table with a laptop"></div>
    <div class="copy right" style="top:34px">
      <h2>Appointments</h2>
      <p>One of the benefits of having an attorney is the ability to discuss your case outside of court, minus the stress and headaches. If you need an appointment, please contact the office.</p>
      <p class="strong">Appointments must be scheduled in advance. We do not want you to make a special trip to the office only to learn that we are in court or otherwise unavailable.</p>
    </div>
  </section>

  <section class="row" style="top:1059px;height:322px">
    <div class="copy left" style="top:35px">
      <h2>Jail Visits</h2>
      <p>If your family member is currently in jail, we take that very seriously. We will visit your loved one and introduce ourselves. While the case is ongoing, we ask that a family member be designated a “contact” person so that messages can be relayed quickly. Never discuss the facts of the case over the phone with someone who is in jail. Jail calls are recorded and we have seen too many cases go south based on remarks made over recorded lines.</p>
    </div>
    <div class="photo right" style="top:33px;background:linear-gradient(100deg,#8a5a3a,#3a2e28 45%,#1a1614)" role="img" aria-label="Photo of a visitor speaking by phone with an inmate through glass"></div>
  </section>

  <section class="row navy" style="top:1381px;height:297px">
    <div class="photo left" style="top:35px;background:linear-gradient(135deg,#7a6350,#e6e2dc 50%,#cfd2d6)" role="img" aria-label="Photo of a case file handed across a desk beside law books and a gavel"></div>
    <div class="copy right" style="top:34px">
      <h2>Police Reports<br>and Discovery</h2>
      <p>We will do our best to provide you with copies of everything we receive on your case. Most information will be emailed, so please keep your email address up to date.</p>
    </div>
  </section>

  <section class="row" style="top:1678px;height:305px">
    <div class="copy left" style="top:40px;width:360px">
      <h2>Changes in Contact Information</h2>
      <p>If you move or change numbers during the case, please let us know. It is difficult to help if we are unable to reach you, and helping you is why we are here.</p>
    </div>
    <div class="photo right" style="top:41px;background:linear-gradient(120deg,#4b4f57,#9ea3aa 50%,#e4e6e8)" role="img" aria-label="Photo of an attorney going over paperwork with a client"></div>
  </section>

  <section class="row teal" style="top:1983px;height:297px">
    <div class="photo left" style="top:35px;background:linear-gradient(135deg,#6b4a32,#8c6b52 45%,#2f3340)" role="img" aria-label="Photo of an attorney addressing a jury in a courtroom"></div>
    <div class="copy right" style="top:35px">
      <h2>Court Appearances</h2>
      <p>Cases do not get resolved as quickly as they do on television. Expect there to be several hearings in your case and it may be necessary for you to attend one or more of them. If a hearing is set, you will receive notice of the date and time of each hearing.</p>
    </div>
  </section>

  <section class="row" style="top:2280px;height:300px">
    <div class="copy left" style="top:39px;width:390px">
      <h2>Billing and<br>Collections</h2>
      <p>We understand that this investment was a huge decision for you. As we focus on providing the best representation, we will need for you to stay on schedule with any payment arrangements agreed to at the time of your initial consultation.</p>
    </div>
    <div class="photo right" style="top:41px;background:linear-gradient(120deg,#dfe3e6,#a9b0b8 50%,#4a4440)" role="img" aria-label="Photo of a man reviewing an invoice on a computer"></div>
  </section>

  <p class="thanks">Again, thank you for your trust in us. We look forward to getting a fantastic outcome on your case.</p>

  <footer class="footer">
    <div class="contact">
      <span class="icon"><svg width="24" height="24" viewBox="0 0 24 24" aria-hidden="true"><path d="M6.6 2.8l3 3.2-1.8 2.6c1 2.3 2.8 4.2 5.3 5.4l2.6-1.8 3.3 3-1.6 3.2C10 18.4 5.6 14 4 6.4z" fill="none" stroke="var(--navy)" stroke-width="1.8" stroke-linejoin="round"/></svg></span>
      (888) 555-0142
    </div>
    <div class="contact">
      <span class="icon"><svg width="24" height="24" viewBox="0 0 24 24" aria-hidden="true"><g fill="none" stroke="var(--navy)" stroke-width="1.6"><circle cx="12" cy="12" r="9"/><ellipse cx="12" cy="12" rx="4" ry="9"/><path d="M3 12h18M5 7h14M5 17h14"/></g></svg></span>
      harlowlegalgroup.com
    </div>
    <div class="contact">
      <span class="icon"><svg width="24" height="24" viewBox="0 0 24 24" aria-hidden="true"><g fill="none" stroke="var(--navy)" stroke-width="1.8" stroke-linejoin="round"><rect x="3" y="6" width="18" height="12"/><path d="M3 6l9 7 9-7"/></g></svg></span>
      info@harlowlegalgroup.com
    </div>
  </footer>
</main>
</body>
</html>
```